Adventure Business Cards

Please check out our website for style
Vertical card
Details:
Side 1
Logo
Business name: Kestrel Bay Wildlife Tours
Name: Colin Marsby
Role: Director
Email: info@kestrelbaywildtours.example
Address: PO Box 71, Fennick Point NSW 2741
Phone: +61 2 5550 4817
Web address: www.kestrelbaywildtours.example
Side 2
Taking pictures?
A Facebook and Instagram logo
Tag us in your pictures with
#kbwildtoursco
@kbwildtoursco
www.kestrelbaywildtours.example
Details:
Side 1
Logo
Name: Colin Marsby
Role: Director
Phone: +61 2 5550 4817
Side 2
Taking pictures?
#kbwildtoursco
@kbwildtoursco

```html
<!DOCTYPE html>
<html lang="en">
<head>
<meta charset="utf-8">
<title>Kestrel Bay Wildlife Tours – Business Card</title>
<link rel="stylesheet" href="https://fonts.googleapis.com/css2?family=Josefin+Sans:wght@400;600;700&family=Kalam:wght@700&display=swap">
<style>
  :root {
    --backdrop: #e7e4df;
    --card: #f7f7f7;
    --card-edge: #dcdcdc;
    --orange: #eba32c;
    --ink: #2b2b2b;
    --grey: #6f6f6f;
    --soft-grey: #8a8a8a;
    --stripe: rgba(0,0,0,0.035);
    --social-blue: #3b5998;
    --social-brown: #8a6a4f;
    --frame: #ffffff;
  }
  * { box-sizing: border-box; margin: 0; padding: 0; }
  html, body { width: 852px; height: 1200px; overflow: hidden; }
  body {
    background: var(--backdrop);
    font-family: "Josefin Sans", sans-serif;
    color: var(--ink);
    position: relative;
  }
  .card {
    position: absolute;
    top: 290px;
    width: 360px;
    height: 620px;
    background: linear-gradient(180deg, #ffffff 0%, var(--card) 60%, #efefef 100%);
    border: 1px solid var(--card-edge);
    border-radius: 18px;
    box-shadow: 0 8px 22px rgba(0,0,0,0.18);
    overflow: hidden;
  }
  .card--front { left: 46px; }
  .card--back { left: 446px; }

  /* Front */
  .person { position: absolute; top: 40px; right: 34px; text-align: right; }
  .person__name { color: var(--orange); font-weight: 700; font-size: 26px; letter-spacing: 0.5px; }
  .person__role { color: var(--grey); font-size: 16px; margin-top: 2px; }

  .brand {
    position: absolute; top: 120px; left: 0; right: 0;
    display: flex; flex-direction: column; align-items: center; gap: 14px;
  }
  .brand__mark { width: 110px; height: 110px; border-radius: 50%; background: var(--ink); }
  .brand__name {
    font-weight: 600; font-size: 20px; color: var(--ink);
    text-align: center; width: 240px; line-height: 1.25;
  }

  .contact { position: absolute; top: 370px; left: 0; right: 0; list-style: none; }
  .contact__row {
    display: flex; align-items: center; gap: 12px;
    height: 44px; padding: 0 26px;
    font-size: 13.5px; color: var(--grey);
  }
  .contact__row:nth-child(odd) { background: var(--stripe); }
  .contact__row--plain { padding-left: 56px; }
  .contact__icon { width: 20px; height: 20px; flex: none; }

  /* Back */
  .headline {
    position: absolute; top: 34px; left: 0; right: 0; text-align: center;
    font-family: "Kalam", cursive; font-size: 34px; color: var(--soft-grey);
  }
  .snapshots { position: absolute; top: 110px; left: 0; width: 360px; height: 270px; }
  .snapshot {
    position: absolute; background: var(--frame);
    padding: 8px 8px 18px; box-shadow: 0 3px 10px rgba(0,0,0,0.22);
  }
  .snapshot__fill { width: 100%; height: 100%; }
  .snapshot--forest { left: 30px; top: 8px; width: 190px; height: 140px; transform: rotate(-6deg); }
  .snapshot--forest .snapshot__fill { background: linear-gradient(160deg, #5e7a4a, #2f4a2a 60%, #a7b59a); }
  .snapshot--bird { left: 175px; top: 40px; width: 160px; height: 150px; transform: rotate(7deg); }
  .snapshot--bird .snapshot__fill { background: linear-gradient(170deg, #5b6674, #33404e 70%, #7d8895); }
  .snapshot--reef { left: 60px; top: 120px; width: 210px; height: 140px; transform: rotate(-2deg); }
  .snapshot--reef .snapshot__fill { background: linear-gradient(150deg, #5fa7b0, #1f5e6b 55%, #c9a07a); }

  .tagline {
    position: absolute; top: 410px; left: 30px;
    font-family: "Kalam", cursive; font-size: 22px; color: var(--ink);
  }
  .social { position: absolute; top: 460px; left: 30px; list-style: none; }
  .social__row { display: flex; align-items: center; gap: 16px; height: 56px; font-size: 22px; color: var(--ink); }
  .social__mark { width: 38px; height: 38px; flex: none; }
  .social__mark--square { background: var(--social-blue); border-radius: 6px; }
  .social__mark--circle { background: var(--social-brown); border-radius: 50%; }
</style>
</head>
<body>

<section class="card card--front" aria-label="Card front">
  <div class="person">
    <p class="person__name">Colin Marsby</p>
    <p class="person__role">Director</p>
  </div>

  <div class="brand">
    <div class="brand__mark"></div>
    <p class="brand__name">Kestrel Bay Wildlife Tours</p>
  </div>

  <ul class="contact">
    <li class="contact__row">
      <svg class="contact__icon" viewBox="0 0 20 20"><rect x="5" y="1" width="10" height="18" rx="2" fill="none" stroke="var(--orange)" stroke-width="2"/><circle cx="10" cy="15.5" r="1" fill="var(--orange)"/></svg>
      +61 2 5550 4817
    </li>
    <li class="contact__row">
      <svg class="contact__icon" viewBox="0 0 20 20"><rect x="1" y="4" width="18" height="12" fill="var(--orange)"/><path d="M1 4 L10 11 L19 4" fill="none" stroke="#fff" stroke-width="1.5"/></svg>
      info@kestrelbaywildtours.example
    </li>
    <li class="contact__row">
      <svg class="contact__icon" viewBox="0 0 20 20"><circle cx="10" cy="10" r="8" fill="none" stroke="var(--orange)" stroke-width="2"/><path d="M2 10 H18 M10 2 C6 6 6 14 10 18 M10 2 C14 6 14 14 10 18" fill="none" stroke="var(--orange)" stroke-width="1.4"/></svg>
      www.kestrelbaywildtours.example
    </li>
    <li class="contact__row">
      <svg class="contact__icon" viewBox="0 0 20 20"><path d="M10 19 C4 12 3 10 3 7.5 A7 7 0 0 1 17 7.5 C17 10 16 12 10 19 Z" fill="var(--orange)"/><circle cx="10" cy="7.5" r="2.5" fill="#fff"/></svg>
      PO Box 71, Fennick Point
    </li>
    <li class="contact__row contact__row--plain">NSW 2741</li>
  </ul>
</section>

<section class="card card--back" aria-label="Card back">
  <h2 class="headline">Taking Pictures ??</h2>

  <div class="snapshots">
    <figure class="snapshot snapshot--forest"><div class="snapshot__fill" role="img" aria-label="Photo of a misty green rainforest"></div></figure>
    <figure class="snapshot snapshot--bird"><div class="snapshot__fill" role="img" aria-label="Photo of a white seabird in flight against a grey sky"></div></figure>
    <figure class="snapshot snapshot--reef"><div class="snapshot__fill" role="img" aria-label="Underwater photo of a striped reef fish"></div></figure>
  </div>

  <p class="tagline">Tag us in your pictures with</p>
  <ul class="social">
    <li class="social__row"><span class="social__mark social__mark--square"></span>#kbwildtoursco</li>
    <li class="social__row"><span class="social__mark social__mark--circle"></span>@kbwildtoursco</li>
  </ul>
</section>

</body>
</html>
```